Harbourline construction company Business card design

I need a business card design for my company. I have a logo but dont have business cards with our logo..

www.harbourlineconstructco.com.au

The logo is on the website

I need the same details as this design I have attached. we have changed the logo and colours. just like the website

Industry/Entity Type

Building

```html
<!DOCTYPE html>
<html lang="en">
<head>
<meta charset="utf-8">
<title>Harbourline Construction – Business Card</title>
<link rel="stylesheet" href="https://fonts.googleapis.com/css2?family=Lora:wght@400;700&display=swap">
<style>
  :root {
    --backdrop: #2a2a2b;
    --card-white: #fbfbfb;
    --brand-blue: #1f6fa3;
    --brand-blue-deep: #15577f;
    --ink: #2b2b2b;
    --muted: #555;
    --sky-top: #2f5fc4;
    --sky-mid: #7aa6e6;
    --villa-warm: #c9a27a;
    --pool-blue: #2f8fd6;
  }
  * { box-sizing: border-box; margin: 0; padding: 0; }
  html, body { width: 1200px; height: 873px; overflow: hidden; }
  body {
    background: var(--backdrop);
    font-family: "Lora", Georgia, serif;
    position: relative;
  }
  .card {
    position: absolute;
    top: 277px;
    width: 520px;
    height: 318px;
    border-radius: 18px;
    overflow: hidden;
    box-shadow: 0 10px 30px rgba(0,0,0,.45);
  }
  /* Front */
  .card-front { left: 60px; }
  .front-photo {
    position: absolute; inset: 0;
    background:
      linear-gradient(180deg, rgba(0,0,0,0) 55%, rgba(47,143,214,.85) 80%, var(--pool-blue) 100%),
      linear-gradient(100deg, var(--sky-top) 0%, var(--sky-mid) 30%, #e6d2b4 48%, var(--villa-warm) 65%, #8a6a4c 85%, #5c4a3c 100%);
  }
  .front-brand-panel {
    position: absolute; left: 0; bottom: 44px;
    width: 250px; height: 150px;
    background: rgba(255,255,255,.82);
    border-radius: 0 18px 18px 0;
    display: flex; flex-direction: column; align-items: center; justify-content: center;
  }
  .brand-name {
    color: var(--brand-blue);
    font-weight: 700;
    font-size: 24px;
    letter-spacing: 1px;
    text-transform: uppercase;
    line-height: 1.1;
    text-align: center;
  }
  .brand-name small { display: block; font-size: 13px; letter-spacing: 5px; }
  .front-tagline {
    position: absolute; left: 0; right: 0; bottom: 0;
    height: 44px;
    display: flex; align-items: center;
    padding-left: 24px;
    color: #fff;
    font-size: 17px;
    letter-spacing: .5px;
  }
  /* Back */
  .card-back { left: 620px; background: var(--card-white); }
  .back-brand { position: absolute; left: 30px; top: 58px; }
  .back-brand .brand-name { text-align: left; font-size: 22px; }
  .holder { position: absolute; right: 30px; top: 62px; text-align: right; }
  .holder-name { color: var(--brand-blue-deep); font-weight: 700; font-size: 22px; }
  .holder-role { color: var(--muted); font-size: 11px; font-family: Arial, sans-serif; }
  .divider {
    position: absolute; left: 30px; right: 30px; top: 150px;
    height: 2px; background: var(--brand-blue);
  }
  .address {
    position: absolute; right: 30px; top: 166px;
    text-align: right; color: var(--brand-blue); font-size: 14px; line-height: 1.5;
  }
  .contacts { position: absolute; left: 30px; bottom: 26px; list-style: none; }
  .contacts li {
    display: flex; align-items: center; gap: 10px;
    color: var(--ink); font-size: 15px; line-height: 1.45;
  }
  .contacts svg { width: 13px; height: 13px; fill: var(--brand-blue); flex: none; }
</style>
</head>
<body>
  <section class="card card-front">
    <div class="front-photo" role="img" aria-label="Photograph of a luxury villa with a lit swimming pool under a blue evening sky"></div>
    <div class="front-brand-panel">
      <p class="brand-name">Harbourline<small>Construction</small></p>
    </div>
    <p class="front-tagline">We build strong and beautiful homes</p>
  </section>

  <section class="card card-back">
    <div class="back-brand">
      <p class="brand-name">Harbourline<small>Construction</small></p>
    </div>
    <div class="holder">
      <p class="holder-name">Marin Calder</p>
      <p class="holder-role">Director</p>
    </div>
    <div class="divider"></div>
    <p class="address">Unit 3 Level 2, 18 Tidewater Rd,<br>Kallaroo, WA 6025</p>
    <ul class="contacts">
      <li><svg viewBox="0 0 12 12" aria-hidden="true"><path d="M3 0h6a1 1 0 0 1 1 1v10a1 1 0 0 1-1 1H3a1 1 0 0 1-1-1V1a1 1 0 0 1 1-1zm0 2v7h6V2z"/></svg>3579140276</li>
      <li><svg viewBox="0 0 12 12" aria-hidden="true"><path d="M1 3c0-1 1-2 5-2s5 1 5 2v1H8V3H4v1H1zm2 2h6l2 6H1z"/></svg>3871352604</li>
      <li><svg viewBox="0 0 12 12" aria-hidden="true"><path d="M3 0h6v4H3zM1 5h10v7H1zm2 2v1h2V7zm4 0v1h2V7z"/></svg>3362718095</li>
      <li><svg viewBox="0 0 12 12" aria-hidden="true"><path d="M0 2h12v8H0zm1 1v.4l5 3.3 5-3.3V3z"/></svg>harbourlinebuildco@gmail.com</li>
    </ul>
  </section>
</body>
</html>
```